Cloud Software Services Business Card Design Challenge

We are seeking a fresh and creative business card design that aligns with the brand identity of a startup cloud software services company. As a company specializing in advanced cloud solutions, we want these business cards to reflect our technological leadership and professionalism, helping us stand out in business communications and emphasize our core values.

About Us: We are dedicated to supporting the digital transformation of interior design companies through efficient, reliable, and innovative cloud software services. Our goal is to provide the best technological solutions to drive continuous growth and success for our clients.

Design Requirements:

• Colors: We have not yet established a final color scheme, so please do not feel constrained by the current logo colors. The logo colors can be adjusted according to the overall design. We would like you to choose colors based on your design concept, considering a minimalist, professional, and high-end palette. While many tech companies use a lot of blue, we prefer to avoid this common approach, so feel free to explore other color options.

• Style: The business card design should be modern, clean, and professional, reflecting our technological leadership and innovation capabilities. The design should have a strong visual impact and showcase our expertise in cloud technology.

• Visual Elements: We want the overall feel to be simple and clean. Consider incorporating technology-inspired design elements, such as sleek lines or geometric shapes, to enhance our brand's modern tech image.

• Final Design: The business card should have clear readability and a logical layout, and be suitable for various physical media. The design should accurately reflect our company's professional image and innovative capabilities in the cloud software services field.

• Information Layout: The card should include the following details (we will provide the details for 1 name after selecting the winner and ask the designer to provide four final information of the same design—
1. Chinese version with the job title
2. Chinese version without the job title
3. English version with the job title
4. English version without the job title
o Name
o Job Title
o Company Name and Address
o Tax ID Number
o Phone Number
o Email Address
o Company Website URL
o QR Code

We look forward to seeing how your design can showcase our excellence and professionalism in the cloud software services industry. We hope your creativity will help us effectively communicate our brand values!

Target Market(s)

Interior Design Companies

Contact Information for Business Card

The card should include the following details (we will provide the details for 1 name after selecting the winner and ask the designer to provide four final information of the same design— 1. Chinese version with the job title 2. Chinese version without the job title 3. English version with the job title 4. English version without the job title o Name o Job Title o Company Name and Address o Tax ID Number o Phone Number o Email Address o Company Website URL o QR Code

Colors
0054AA
0677BA
7BADD7
CADEEF
E8F1F8
0094D4
00A9DD
6FCCEA
C7EBF8
E9F6FB
00AB8E
00BBA5
67D7C9
C6EFE9
E9F9F6
FFC000
F8CF3A
FAE287
FDF2CF
FEFAEE
F0912C
F2A743
F7CA91
FBE8D2
FDF5EE
EE7325
F08F49
F5BC92
FAE3D3
FDF4ED
A7469A
B969AE
D3A5CF
EDDBEB
F8F0F9
6B429C
8869AF
B7A5CE
E3DAEB
F3F0F8

```html
<!DOCTYPE html>
<html lang="en">
<head>
<meta charset="utf-8">
<title>Veltrix Business Card</title>
<link href="https://fonts.googleapis.com/css2?family=Michroma&family=Arimo:wght@400;700&display=swap" rel="stylesheet">
<style>
  :root {
    --backdrop: #3c3c3c;
    --accent: #e3531f;
    --paper: #ffffff;
    --ink: #2a2a2a;
    --muted: #555555;
    --card-dark: #2b2b2b;
    --back-text: #8c8c8c;
  }
  html, body {
    margin: 0;
    width: 1200px;
    height: 803px;
    overflow: hidden;
    background: var(--backdrop);
  }
  .canvas {
    position: relative;
    width: 1200px;
    height: 803px;
  }
  .card {
    position: absolute;
    top: 252px;
    width: 525px;
    height: 300px;
    border-radius: 18px;
    overflow: hidden;
    box-shadow: 0 4px 0 var(--accent), 0 18px 36px rgba(0,0,0,0.35);
  }
  .card--front { left: 50px; background: var(--paper); }
  .card--back { left: 625px; background: var(--card-dark); }

  .front-band {
    position: absolute;
    inset: 0;
    width: 525px;
    height: 300px;
  }
  .front-band polygon { fill: var(--accent); }

  .company-name {
    position: absolute;
    margin: 0;
    font-family: "Arimo", sans-serif;
    font-weight: 700;
    letter-spacing: 0.04em;
    white-space: nowrap;
  }
  .company-name--front {
    top: 38px;
    right: 32px;
    font-size: 28px;
    color: var(--ink);
  }
  .company-name--back {
    top: 50%;
    left: 50%;
    transform: translate(-50%, -50%);
    font-size: 38px;
    color: var(--back-text);
  }

  .person {
    position: absolute;
    left: 30px;
    top: 64px;
  }
  .person__name {
    margin: 0;
    font-family: "Michroma", sans-serif;
    font-size: 18px;
    color: var(--accent);
    letter-spacing: 0.04em;
  }
  .person__role {
    margin: 4px 0 0;
    font-family: "Arimo", sans-serif;
    font-size: 12px;
    color: var(--muted);
  }

  .address, .contacts {
    position: absolute;
    font-family: "Arimo", sans-serif;
    font-size: 13px;
    line-height: 1.45;
    color: var(--paper);
    margin: 0;
    font-style: normal;
  }
  .address { left: 30px; top: 208px; }
  .contacts {
    left: 268px;
    top: 196px;
    list-style: none;
    padding: 0;
  }
  .contacts li {
    display: flex;
    align-items: center;
    gap: 8px;
    margin-bottom: 4px;
  }
  .contacts svg { width: 12px; height: 12px; fill: var(--paper); flex: none; }
</style>
</head>
<body>
<main class="canvas">
  <section class="card card--front" aria-label="Card front">
    <svg class="front-band" viewBox="0 0 525 300" aria-hidden="true">
      <polygon points="0,178 525,88 525,300 0,300"/>
    </svg>
    <p class="company-name company-name--front">VELTRIX</p>
    <div class="person">
      <p class="person__name">DANIEL MOREAU</p>
      <p class="person__role">President</p>
    </div>
    <address class="address">412 Cedar Ridge Road<br>Halden, Canada 50218</address>
    <ul class="contacts">
      <li><svg viewBox="0 0 12 12"><path d="M2.5 0.8l2 2-1 1.3c.6 1.4 1.9 2.7 3.3 3.3l1.3-1 2 2-1.2 1.8C5 10 2 7 .8 2z"/></svg>555-210-4471</li>
      <li><svg viewBox="0 0 12 12"><path d="M0 2h12v8H0z M1 3l5 3.5L11 3v-.2H1z" fill-rule="evenodd"/></svg>info@veltrix.com</li>
      <li><svg viewBox="0 0 12 12"><circle cx="6" cy="6" r="5.5"/></svg>www.veltrix.com</li>
    </ul>
  </section>

  <section class="card card--back" aria-label="Card back">
    <p class="company-name company-name--back">VELTRIX</p>
  </section>
</main>
</body>
</html>
```